Cloud Phone Service Brochure

We need a brochure for a Cloud Phone Service offering that we offer in Canada. We're a small company that cares about our client's success and protects their privacy. We would like to see designs that reflect us as a stable, trustworthy company which is also fast moving and leading edge. We see ourselves more like Zelmo than Hask. Sketch Harbor has built our logo and business card, and we look forward to moving ahead here. I've attached our Business Card file so you have our logo as well as my own shot at some thoughts about content written as a trifold. That specific content does not need to be used, nor does it need to be a trifold. Those phone pictures are the actual phones we use.

```html
<!DOCTYPE html>
<html lang="en">
<head>
<meta charset="utf-8">
<title>Northbeam Consulting – Cloud Phone Service Trifold</title>
<link href="https://fonts.googleapis.com/css2?family=Oswald:wght@400;600&family=Open+Sans:wght@400;600;700&family=Raleway:wght@500&display=swap" rel="stylesheet">
<style>
  :root{
    --blue:#1ba1e2;
    --blue-deep:#1590d0;
    --slate:#36424c;
    --slate-dark:#262f37;
    --ink:#2b3238;
    --paper:#ffffff;
    --mist:#e7e9eb;
    --stage:#e4e4e4;
  }
  *{box-sizing:border-box;margin:0;padding:0}
  html,body{width:1200px;height:1200px;overflow:hidden;background:var(--stage)}
  body{font-family:"Open Sans",Arial,sans-serif;color:var(--ink)}
  .brochure{position:absolute;left:60px;top:218px;width:1080px;height:763px;display:flex;box-shadow:0 18px 30px rgba(0,0,0,.25)}
  .panel{position:relative;width:360px;height:763px;overflow:hidden}
  .panel--services{background:var(--paper)}
  .panel--about{background:var(--slate)}
  .panel--cover{background:var(--slate)}
  .abs{position:absolute}
  .wordmark{font-family:"Raleway",Arial,sans-serif;font-weight:500;letter-spacing:.5px;display:flex;align-items:center;gap:10px;white-space:nowrap}
  .wordmark__dot{width:14px;height:14px;background:var(--blue)}
  .photo{position:absolute}
  /* services panel */
  .hero-title{left:80px;top:6px;font-family:"Oswald",Arial,sans-serif;color:var(--blue);line-height:1}
  .hero-title__lead{font-size:24px;font-weight:400}
  .hero-title__main{font-size:38px;font-weight:600;letter-spacing:-.5px;color:var(--blue-deep)}
  .photo--desk-phone{left:0;top:82px;width:360px;height:240px;background:linear-gradient(120deg,#f3f4f5 0%,#c9ccd0 40%,#4c4f54 70%,#e9e2da 100%)}
  .divider-bar{left:0;top:318px;width:360px;height:8px;background:var(--blue)}
  .divider-bar::after{content:"";position:absolute;left:180px;top:0;width:120px;height:8px;border-radius:4px;background:var(--slate)}
  .section-title{font-size:13.5px;font-weight:700;color:var(--blue);letter-spacing:.2px}
  .features{left:17px;top:348px}
  .check-list{list-style:none;font-size:9.6px;line-height:1.1}
  .check-list li{position:relative;padding-left:16px;margin-bottom:7px}
  .check-list li::before{content:"";position:absolute;left:0;top:3px;width:9px;height:5px;background:var(--slate);clip-path:polygon(0 100%,40% 0,60% 0,100% 100%)}
  .features__cols{display:flex;gap:12px;margin-top:10px}
  .features__cols .check-list{width:150px}
  .help{left:17px;top:518px}
  .help .check-list{margin-top:10px;width:150px}
  .photo--handset{left:222px;top:542px;width:70px;height:78px;border-radius:6px;background:linear-gradient(160deg,#4a4f55,#1d2125)}
  .photo--energy{left:208px;top:625px;width:124px;height:54px;background:linear-gradient(180deg,#9fd3f3 0%,#cfe9f6 45%,#7fb35a 75%,#3d74a8 100%)}
  .pledge{left:20px;top:628px;font-size:9.4px;font-weight:700;line-height:1.3}
  .footer-band{left:0;top:686px;width:360px;height:77px;background:var(--mist);display:flex;align-items:center;justify-content:center}
  .footer-band .wordmark{font-size:16px;color:var(--slate)}
  /* about panel */
  .about{left:28px;top:26px;width:304px;text-align:center}
  .about__title{font-size:15px;font-weight:700;color:var(--blue)}
  .about__text{font-size:10.6px;line-height:1.35;color:#eef2f5;margin-top:8px}
  .partners{left:20px;top:160px;width:320px;text-align:center}
  .partners__title{font-size:15px;font-weight:700;color:var(--blue)}
  .partners__grid{display:grid;grid-template-columns:repeat(3,88px);gap:18px 20px;justify-content:center;margin-top:16px}
  .badge{height:26px;border-radius:4px;background:rgba(255,255,255,.16)}
  .badge--light{background:rgba(255,255,255,.26)}
  .brand-band{left:0;top:378px;width:360px;height:172px;background:var(--slate-dark);display:flex;align-items:center;justify-content:center}
  .brand-band .wordmark{font-size:21px;color:#fff}
  .contact{left:0;width:360px;text-align:center;color:#fff}
  .contact__label{font-size:11px;font-weight:600;color:var(--blue);display:inline-flex;align-items:center;gap:4px}
  .contact__value{font-size:11px;font-weight:600;line-height:1.35;margin-top:4px}
  .contact__rule{width:112px;margin:8px auto 0;border-top:1px dashed rgba(255,255,255,.6)}
  .web{left:0;width:360px;top:732px;text-align:center;font-size:14px;color:#fff;display:flex;justify-content:center;align-items:center;gap:5px}
  .web__dot{width:6px;height:6px;border-radius:50%;background:var(--blue)}
  .web b{font-weight:400;color:var(--blue)}
  /* cover panel */
  .cover-top{left:0;top:0;width:360px;height:138px;background:var(--paper);display:flex;align-items:center;justify-content:center;border-bottom:4px solid var(--blue)}
  .cover-top .wordmark{font-size:22px;color:var(--slate)}
  .photo--portrait{left:0;top:142px;width:360px;height:440px;background:linear-gradient(150deg,#e9ebe8 0%,#c7c3bb 40%,#8c8f93 70%,#e3e4e1 100%)}
  .tagline-band{left:0;top:590px;width:360px;height:118px;background:var(--blue);color:#fff;text-align:center;font-family:"Oswald",Arial,sans-serif;line-height:1;padding-top:22px;border-bottom:3px solid #fff}
  .tagline-band__lead{font-size:27px;font-weight:400;letter-spacing:.5px}
  .tagline-band__main{font-size:42px;font-weight:600;margin-top:4px}
</style>
</head>
<body>
<main class="brochure">

  <section class="panel panel--services">
    <div class="photo photo--desk-phone" role="img" aria-label="Photo of a hand dialing a desk phone with the handset lifted"></div>
    <h2 class="abs hero-title"><span class="hero-title__lead">WE PROVIDE YOU</span><br><span class="hero-title__main">BESTSERVICES</span></h2>
    <div class="abs divider-bar"></div>

    <div class="abs features">
      <h3 class="section-title">PHONE SERVICE FEATURES</h3>
      <div class="features__cols">
        <ul class="check-list">
          <li>All features and functions included</li>
          <li>Monthly billing with no contract</li>
          <li>Voicemail to email</li>
          <li>Conference line included</li>
          <li>Any high speed internet service</li>
          <li>Find Me &amp; Follow Me</li>
        </ul>
        <ul class="check-list">
          <li>Toll Free Number included</li>
          <li>No hardware or installation costs</li>
          <li>Call Recording</li>
          <li>North American LD included</li>
          <li>Keep your existing phone number</li>
        </ul>
      </div>
    </div>

    <div class="abs help">
      <h3 class="section-title">WE GIVE OUR TIME AND SKILLS TO HELP</h3>
      <ul class="check-list">
        <li>Schools</li>
        <li>Community Associations</li>
        <li>Non-profits</li>
        <li>Renewable Energy Initiatives</li>
      </ul>
    </div>
    <div class="photo photo--handset" role="img" aria-label="Photo of an office IP desk phone"></div>
    <div class="photo photo--energy" role="img" aria-label="Illustration of solar panels and wind turbines in a green landscape"></div>
    <p class="abs pledge">We Are 70% Renewable Energy &amp;<br>100% Renewable for 2020</p>

    <div class="abs footer-band"><div class="wordmark"><span class="wordmark__dot"></span>Northbeam Consulting</div></div>
  </section>

  <section class="panel panel--about">
    <div class="abs about">
      <h3 class="about__title">ABOUT NORTHBEAM</h3>
      <p class="about__text">is simply dummy text of the printing and typesetting industry. Lorem Ipsum has been the industry's standard dummy text ever since the 1500s, when an unknown printer took a galley of type and scrambled it to make a type specimen book. It has survived not only</p>
    </div>
    <div class="abs partners">
      <h3 class="partners__title">OUR PARTNERS</h3>
      <div class="partners__grid" aria-label="Partner badges">
        <span class="badge"></span><span class="badge badge--light"></span><span class="badge"></span>
        <span class="badge badge--light"></span><span class="badge"></span><span class="badge badge--light"></span>
        <span class="badge"></span><span class="badge badge--light"></span><span class="badge"></span>
      </div>
    </div>
    <div class="abs brand-band"><div class="wordmark"><span class="wordmark__dot"></span>Northbeam Consulting</div></div>

    <div class="abs contact" style="top:578px">
      <div class="contact__label">ADRESS
        <svg width="8" height="10" viewBox="0 0 8 10"><path d="M4 0a4 4 0 0 0-4 4c0 3 4 6 4 6s4-3 4-6a4 4 0 0 0-4-4zm0 5.5A1.5 1.5 0 1 1 4 2.5a1.5 1.5 0 0 1 0 3z" fill="#fff"/></svg>
      </div>
      <p class="contact__value">44-8810 Larchmont Ridge Road NW Calgary,<br>Alberta T3R 2K7 Canada</p>
      <div class="contact__rule"></div>
    </div>
    <div class="abs contact" style="top:655px">
      <div class="contact__label">PHONE
        <svg width="10" height="9" viewBox="0 0 10 9"><path d="M1 3c0-2 8-2 8 0v1H7V3H3v1H1zM2 5h6l1 4H1z" fill="#fff"/></svg>
      </div>
      <p class="contact__value">(403)555-0148</p>
      <div class="contact__rule"></div>
    </div>
    <p class="abs web"><span class="web__dot"></span>www.<b>northbeamconsult</b>.com</p>
  </section>

  <section class="panel panel--cover">
    <div class="abs cover-top"><div class="wordmark"><span class="wordmark__dot"></span>Northbeam Consulting</div></div>
    <div class="photo photo--portrait" role="img" aria-label="Photo of a smiling woman in glasses talking on a desk phone while taking notes"></div>
    <div class="abs tagline-band">
      <div class="tagline-band__lead">FAST MOVING &amp;</div>
      <div class="tagline-band__main">LEADING EDGE</div>
    </div>
    <p class="abs web"><span class="web__dot"></span>www.<b>northbeamconsult</b>.com</p>
  </section>

</main>
</body>
</html>
```